Vehicle Signage Design for a Renovation Company

We're a renovation company specialising in Home Renovations. The final design should communicate trust, credibility, and confidence. We need vehicle signage designed for our company utes (see attachment) / for our grey ute with the canopy/ and white use withou the canopyI've also attached our existing designs for the current vehicles (van and hatch back) to give you an idea of what we're after.In terms of content, there isn't much requirement for this due to the limited space on the ute - but happy to hear ideas on this.We've tried designing it ourselves - see attachment, but not happy with the result, would like more variations and ideas.Check out our website www.kestrelrenovations.co.nz for ideas on our branding/ style.
Updates

Target Market(s)

Home Owners

Industry/Entity Type

Residential Construction

Font styles to use
Sans Serif

Colors
3276b5
0355a3
33a6d7
3aa7d7
ffffff

Requirements
Must have
• Logo, Call to Action (website and number), Headline
Nice to have
• Strong sharp lines, a clean/sleek look
• It would be nice to have our offer on there (free design plans) / but we know space is limited

```html
<!DOCTYPE html>
<html lang="en">
<head>
<meta charset="utf-8">
<title>Kestrel Home Renovations – Ute Signage</title>
<link href="https://fonts.googleapis.com/css2?family=Montserrat:wght@400;600;700;800&display=swap" rel="stylesheet">
<style>
  :root {
    --blue-deep: #0a2fa8;
    --blue-main: #0b4fc0;
    --blue-bright: #1f5fd6;
    --blue-light: #2a6be6;
    --silver: #d6d8dd;
    --silver-light: #eeeff2;
    --glass: #c3cdcd;
    --glass-dark: #3b4046;
    --tyre: #1c1e22;
    --rim: #b9bcc1;
    --ink: #1d232b;
    --white: #ffffff;
  }
  html, body {
    margin: 0;
    padding: 0;
    width: 1200px;
    height: 603px;
    overflow: hidden;
    background: var(--white);
    font-family: "Montserrat", sans-serif;
  }
  .wrap-layout {
    position: relative;
    width: 1200px;
    height: 603px;
  }
  .wrap-layout svg.panels {
    position: absolute;
    inset: 0;
  }
  .headline-kicker {
    position: absolute;
    left: 264px;
    top: 248px;
    width: 100px;
    text-align: right;
    color: var(--white);
    font-size: 11.5px;
    font-weight: 400;
    letter-spacing: 0.4px;
  }
  .headline {
    position: absolute;
    left: 148px;
    top: 262px;
    color: var(--white);
    font-size: 23px;
    font-weight: 700;
    white-space: nowrap;
  }
  .brand-name {
    position: absolute;
    left: 356px;
    top: 280px;
    width: 250px;
    text-align: right;
    color: var(--blue-bright);
    font-size: 56px;
    font-weight: 800;
    line-height: 1;
  }
  .brand-tagline {
    position: absolute;
    left: 440px;
    top: 343px;
    width: 165px;
    text-align: right;
    color: var(--ink);
    font-size: 12px;
    font-weight: 700;
    white-space: nowrap;
  }
  .web-address {
    position: absolute;
    left: 380px;
    top: 363px;
    width: 224px;
    text-align: right;
    color: var(--white);
    font-size: 12px;
    font-weight: 600;
    white-space: nowrap;
  }
  .phone-number {
    position: absolute;
    left: 398px;
    top: 393px;
    width: 202px;
    text-align: right;
    color: var(--white);
    font-size: 27px;
    font-weight: 700;
    letter-spacing: 0.5px;
    white-space: nowrap;
  }
</style>
</head>
<body>
<main class="wrap-layout">
  <svg class="panels" width="1200" height="603" viewBox="0 0 1200 603" aria-hidden="true">
    <!-- body panel -->
    <path fill="var(--blue-main)" d="M57 432 L57 338 Q60 300 92 284 L325 232 L470 145 Q490 136 520 134 L800 127 Q815 130 818 160 L822 240 L1138 240 Q1146 243 1147 262 L1148 358 Q1156 362 1156 382 Q1154 404 1116 408 L1100 420 L1040 430 L820 438 L366 446 L130 440 Z"/>
    <!-- silver sweep -->
    <path fill="var(--silver)" d="M96 300 C220 292 330 296 372 290 C470 284 560 270 642 244 L816 140 L818 205 L770 378 L400 392 Q360 400 347 441 L130 440 L108 330 Z"/>
    <path fill="var(--silver-light)" opacity="0.6" d="M660 242 L810 152 L812 198 L780 238 Z"/>
    <!-- upper cab dark accent -->
    <path fill="var(--blue-deep)" d="M765 130 L800 127 Q815 130 816 150 Q790 210 740 250 L700 258 Q740 200 765 130 Z"/>
    <!-- lower sill band -->
    <path fill="var(--blue-deep)" d="M347 446 Q362 398 400 392 L780 382 L800 436 Z"/>
    <!-- web address strip -->
    <path fill="var(--blue-bright)" d="M378 363 L612 361 L612 381 L372 384 Q374 371 378 363 Z"/>
    <!-- rear sweep -->
    <path fill="var(--blue-light)" opacity="0.8" d="M800 300 Q880 272 980 276 Q1060 300 1147 318 L1148 410 L780 440 Q790 340 800 300 Z"/>
    <!-- bed pinstripes -->
    <path fill="var(--blue-deep)" d="M912 242 L1140 240 L1140 248 L928 250 Q910 262 900 298 L886 298 Q896 254 912 242 Z"/>
    <path fill="var(--silver)" d="M938 256 L1140 254 L1140 262 L952 264 Q934 274 928 298 L918 298 Q922 266 938 256 Z"/>
    <!-- windows -->
    <path fill="var(--glass)" d="M389 256 L440 190 L470 160 L612 148 L600 246 Z"/>
    <path fill="var(--glass-dark)" opacity="0.35" d="M560 152 L612 148 L600 246 L560 248 Z"/>
    <path fill="var(--glass)" d="M640 145 L771 145 Q780 150 778 211 L769 239 L640 242 Z"/>
    <path fill="var(--glass-dark)" opacity="0.35" d="M700 145 L771 145 Q780 150 778 211 L769 239 L700 240 Z"/>
    <!-- wheel wells -->
    <path fill="var(--tyre)" d="M140 446 Q140 330 240 326 Q340 330 345 446 Z"/>
    <path fill="var(--tyre)" d="M825 446 Q826 322 922 318 Q1020 322 1024 446 Z"/>
    <!-- wheels -->
    <circle cx="240" cy="446" r="86" fill="var(--tyre)"/>
    <circle cx="240" cy="446" r="52" fill="var(--rim)"/>
    <circle cx="240" cy="446" r="12" fill="var(--glass-dark)"/>
    <circle cx="922" cy="446" r="86" fill="var(--tyre)"/>
    <circle cx="922" cy="446" r="52" fill="var(--rim)"/>
    <circle cx="922" cy="446" r="12" fill="var(--glass-dark)"/>
    <!-- brand mark area -->
    <rect x="628" y="262" width="140" height="140" fill="var(--white)"/>
  </svg>

  <div class="headline-kicker">THE BEST</div>
  <div class="headline">Home Renovations</div>

  <div class="brand-name">Kestrel</div>
  <div class="brand-tagline">HOME RENOVATIONS</div>

  <div class="web-address">www.kestrelrenovations.co.nz</div>
  <div class="phone-number">0800 555 014</div>
</main>
</body>
</html>
```